Business Card Design Project

We need a simple business card design that uses our current logo.
We need to have the current logo put into a high res format.
We need to have 1 card made with contact information.
We will supply the information for the 4 employees.
Industry/Entity Type
Business
Requirements
Must have
- The contact information is as follows:
Mark Dellweather
Producer/CEO
c. 949-555-0147
f. 650-555-0193
markd@lanternbay.example
Al Vostrand, CFO
c. 949-555-0162
f. 650-555-0193
alv@lanternbay.example
Peter Malvane, PR
c. 267-555-0128
f. 650-555-0193
pmalvane@lanternbay.example
Tim Garrowby, Producer
c. 949-555-0184
f. 650-555-0193
timg@lanternbay.example
The address for all cards is:
318 W Calle Norvento #2715, San Clemente, CA 92681

```html
<!DOCTYPE html>
<html lang="en">
<head>
<meta charset="utf-8">
<title>Lantern Bay Media — Business Card</title>
<link rel="stylesheet" href="https://fonts.googleapis.com/css2?family=Arimo:wght@400;700&family=Noto+Serif:wght@700&display=swap">
<style>
  :root {
    --stage: #3b3b3d;
    --card-edge: #050505;
    --card-face: #8ca7d0;
    --ink-light: #ffffff;
    --ink-dark: #16243d;
    --ghost: rgba(40, 62, 100, 0.13);
  }
  * { margin: 0; padding: 0; box-sizing: border-box; }
  html, body {
    width: 1200px; height: 800px; overflow: hidden;
    background: var(--stage);
  }
  .stage {
    position: relative; width: 1200px; height: 800px;
    display: flex; align-items: center; justify-content: center; gap: 60px;
  }
  .card {
    position: relative; width: 490px; height: 280px;
    background: var(--card-face);
    border: 12px solid var(--card-edge);
    overflow: hidden;
  }
  /* Contact side */
  .card-contact__ghost {
    position: absolute; left: 0; right: 0; top: 50%;
    transform: translateY(-50%);
    text-align: center;
    font-family: "Arimo", sans-serif; font-weight: 700;
    font-size: 38px; letter-spacing: 0; text-transform: uppercase;
    color: var(--ghost); white-space: nowrap;
  }
  .card-contact__body {
    position: absolute; inset: 0;
    display: flex; align-items: center; padding: 0 22px;
  }
  .identity { width: 196px; flex: none; text-align: right; padding-right: 14px; }
  .identity__name {
    font-family: "Noto Serif", serif; font-weight: 700;
    font-size: 18px; color: var(--ink-light); white-space: nowrap;
  }
  .identity__title {
    font-family: "Arimo", sans-serif; font-size: 13px;
    color: var(--ink-light); margin-top: 4px;
  }
  .divider { width: 2px; height: 130px; flex: none; background: var(--ink-light); }
  .details { list-style: none; padding-left: 14px; }
  .details__item {
    display: flex; align-items: flex-start; gap: 9px;
    font-family: "Arimo", sans-serif; font-size: 12px; line-height: 1.3;
    color: var(--ink-light); margin: 7px 0; white-space: nowrap;
  }
  .details__icon { width: 15px; height: 15px; flex: none; margin-top: 1px; }
  /* Logo side */
  .card-logo { display: flex; align-items: center; justify-content: center; }
  .card-logo__name {
    font-family: "Arimo", sans-serif; font-weight: 700;
    font-size: 40px; text-transform: uppercase; letter-spacing: 1px;
    color: var(--ink-dark); white-space: nowrap;
  }
</style>
</head>
<body>
<main class="stage">
  <section class="card card-contact" aria-label="Card contact side">
    <div class="card-contact__ghost" aria-hidden="true">Lantern Bay Media</div>
    <div class="card-contact__body">
      <div class="identity">
        <p class="identity__name">Mark Dellweather</p>
        <p class="identity__title">Producer/CEO</p>
      </div>
      <div class="divider"></div>
      <ul class="details">
        <li class="details__item">
          <svg class="details__icon" viewBox="0 0 16 16" aria-hidden="true"><path d="M8 2 1 8h2v6h4v-4h2v4h4V8h2z" fill="#fff"/></svg>
          <span>318 W Calle Norvento #2715,<br>San Clemente, CA 92681</span>
        </li>
        <li class="details__item">
          <svg class="details__icon" viewBox="0 0 16 16" aria-hidden="true"><rect x="1" y="1" width="14" height="14" rx="3" fill="#fff"/><path d="M5 4c-1 1-1 3 1 5s4 3 5 2l-1.5-1.5-1 .8C7.6 9.8 6.5 8.7 6 7.8l.8-1z" fill="#8ca7d0"/></svg>
          <span>949-555-0147</span>
        </li>
        <li class="details__item">
          <svg class="details__icon" viewBox="0 0 16 16" aria-hidden="true"><rect x="2" y="6" width="12" height="8" fill="#fff"/><rect x="4" y="1" width="8" height="6" fill="none" stroke="#fff" stroke-width="1.5"/><rect x="4" y="9" width="5" height="1.4" fill="#8ca7d0"/></svg>
          <span>650-555-0193</span>
        </li>
        <li class="details__item">
          <svg class="details__icon" viewBox="0 0 16 16" aria-hidden="true"><rect x="1" y="3" width="14" height="10" fill="#fff"/><path d="M1 3l7 6 7-6" fill="none" stroke="#8ca7d0" stroke-width="1.3"/></svg>
          <span>markd@lanternbay.example</span>
        </li>
      </ul>
    </div>
  </section>

  <section class="card card-logo" aria-label="Card logo side">
    <p class="card-logo__name">Lantern Bay Media</p>
  </section>
</main>
</body>
</html>
```